FLUSH FAIRY the solution to twinkle the smell away...because everyone poops

I need a label for my handmade poop spray. Flush fairy is an organic blend of essential oils that eliminates the odor when you poop. Directions must be on the back of the label : shake well before each use. Spray on the toilet water surface 4-6 times to cover the water before you go. Poop as usual and flush. Safe for all pipes and sewer systems. To order visit my Norvo shop enter flush fairy

Font styles to use
Decorative

Requirements
Must have
• Directions on how to use
Nice to have
• Elegant design label. Product is meant to be kept in the bathroom

```html
<!DOCTYPE html>
<html lang="en">
<head>
<meta charset="utf-8">
<title>Flush Fairy – Label Front and Back</title>
<link rel="stylesheet" href="https://fonts.googleapis.com/css2?family=Arimo&family=Berkshire+Swash&family=Architects+Daughter&family=Open+Sans:wght@700&family=Pinyon+Script&display=swap">
<style>
  :root {
    --paper: #ffffff;
    --ink: #000000;
    --label-black: #1b1b1b;
    --label-deep: #0d0d0d;
    --panel-top: #2e2e2e;
    --panel-bottom: #161616;
    --gold: #d9b24a;
    --gold-light: #f4e08c;
    --gold-dark: #8a6418;
    --cream: #f1ece0;
    --aqua: #5cc4d6;
    --blossom: #f2b8c8;
    --ornament: #b8913a;
    --damask: #2a2a2a;
  }
  html, body {
    margin: 0;
    padding: 0;
    overflow: hidden;
    background: var(--paper);
  }
  .canvas {
    position: relative;
    width: 1200px;
    height: 1000px;
    overflow: hidden;
    background: var(--paper);
  }
  .artboard { display: block; }
  .side-title {
    font-family: "Arimo", Arial, sans-serif;
    font-size: 44px;
    fill: var(--ink);
  }
  .brand-name {
    font-family: "Pinyon Script", cursive;
    font-size: 64px;
    fill: var(--gold);
  }
  .ribbon-text {
    font-family: "Berkshire Swash", cursive;
    font-size: 19px;
    fill: var(--ink);
    letter-spacing: 0.5px;
  }
  .intro-text {
    font-family: "Berkshire Swash", cursive;
    font-size: 15px;
    fill: var(--cream);
    letter-spacing: 0.4px;
  }
  .directions-heading {
    font-family: "Open Sans", Arial, sans-serif;
    font-weight: 700;
    font-size: 17px;
    fill: var(--aqua);
  }
  .directions-text {
    font-family: "Architects Daughter", cursive;
    font-size: 17px;
    fill: var(--cream);
  }
  .keep-text {
    font-family: "Berkshire Swash", cursive;
    font-size: 16px;
    fill: #ffffff;
    letter-spacing: 0.4px;
  }
  .order-text {
    font-family: "Berkshire Swash", cursive;
    font-size: 15px;
    fill: var(--aqua);
    letter-spacing: 0.3px;
  }
</style>
</head>
<body>
<div class="canvas">
  <svg class="artboard" width="1200" height="1000" viewBox="0 0 1200 1000" xmlns="http://www.w3.org/2000/svg">
    <defs>
      <linearGradient id="goldRim" x1="0" y1="0" x2="1" y2="1">
        <stop offset="0" stop-color="var(--gold-dark)"/>
        <stop offset="0.45" stop-color="var(--gold-light)"/>
        <stop offset="1" stop-color="var(--gold-dark)"/>
      </linearGradient>
      <linearGradient id="ribbonGold" x1="0" y1="0" x2="1" y2="0">
        <stop offset="0" stop-color="#c9962e"/>
        <stop offset="0.5" stop-color="var(--gold-light)"/>
        <stop offset="1" stop-color="#c9962e"/>
      </linearGradient>
      <radialGradient id="ovalFace" cx="0.45" cy="0.35" r="0.75">
        <stop offset="0" stop-color="var(--panel-top)"/>
        <stop offset="1" stop-color="var(--label-deep)"/>
      </radialGradient>
      <linearGradient id="backPanel" x1="0" y1="0" x2="0" y2="1">
        <stop offset="0" stop-color="var(--panel-top)"/>
        <stop offset="1" stop-color="var(--panel-bottom)"/>
      </linearGradient>
    </defs>

    <!-- Headings -->
    <text class="side-title" x="355" y="128" text-anchor="middle">Front Side :</text>
    <text class="side-title" x="870" y="128" text-anchor="middle">Back Side :</text>

    <!-- ===== Front label ===== -->
    <g class="front-label">
      <rect class="capsule-outer" x="188" y="205" width="280" height="592" rx="140" fill="var(--label-black)" stroke="#000" stroke-width="2"/>
      <rect class="capsule-inner" x="226" y="240" width="204" height="522" rx="102" fill="var(--damask)" stroke="url(#goldRim)" stroke-width="3"/>
      <rect class="ornament-top" role="img" aria-label="Gold filigree ornament on damask pattern" x="272" y="250" width="112" height="88" rx="40" fill="var(--ornament)" opacity="0.55"/>
      <rect class="ornament-bottom" role="img" aria-label="Gold filigree ornament on damask pattern" x="272" y="665" width="112" height="85" rx="40" fill="var(--ornament)" opacity="0.55"/>

      <ellipse class="oval-rim" cx="328" cy="495" rx="200" ry="160" fill="url(#goldRim)"/>
      <ellipse class="oval-face" cx="328" cy="495" rx="190" ry="151" fill="url(#ovalFace)"/>
      <ellipse class="oval-inner-line" cx="328" cy="495" rx="178" ry="140" fill="none" stroke="url(#goldRim)" stroke-width="2"/>

      <rect class="blossom" role="img" aria-label="Pink cherry blossom flowers" x="380" y="398" width="84" height="80" rx="38" fill="var(--blossom)"/>

      <text class="brand-name" x="330" y="515" text-anchor="middle">Flush Fairy</text>
      <line class="title-rule" x1="194" y1="543" x2="465" y2="543" stroke="url(#goldRim)" stroke-width="4"/>
      <rect class="ornament-divider" role="img" aria-label="Small gold scroll ornament" x="268" y="553" width="124" height="26" rx="12" fill="var(--ornament)" opacity="0.7"/>

      <g class="ribbon" transform="rotate(-8 312 655)">
        <polygon points="150,633 185,633 185,665 150,665 162,649" fill="#b98424"/>
        <polygon points="438,633 474,633 462,649 474,665 438,665" fill="#b98424"/>
        <rect x="178" y="630" width="266" height="40" fill="url(#ribbonGold)" stroke="var(--gold-dark)" stroke-width="1"/>
        <text class="ribbon-text" x="311" y="657" text-anchor="middle">handmade poop spray</text>
      </g>
    </g>

    <!-- ===== Back label ===== -->
    <g class="back-label">
      <rect class="card" x="686" y="205" width="388" height="590" rx="14" fill="var(--label-black)" stroke="#000" stroke-width="2"/>
      <rect class="frame-outer" x="695" y="215" width="370" height="570" rx="10" fill="none" stroke="url(#goldRim)" stroke-width="3"/>
      <rect class="frame-mid" x="705" y="225" width="350" height="550" rx="8" fill="none" stroke="var(--gold)" stroke-width="1.5"/>

      <rect class="corner-ornament" role="img" aria-label="Gold art nouveau corner scroll" x="705" y="226" width="70" height="62" rx="10" fill="var(--ornament)" opacity="0.6"/>
      <rect class="corner-ornament" role="img" aria-label="Gold art nouveau corner scroll" x="985" y="226" width="70" height="62" rx="10" fill="var(--ornament)" opacity="0.6"/>
      <rect class="corner-ornament" role="img" aria-label="Gold art nouveau corner scroll" x="705" y="712" width="70" height="62" rx="10" fill="var(--ornament)" opacity="0.6"/>
      <rect class="corner-ornament" role="img" aria-label="Gold art nouveau corner scroll" x="985" y="712" width="70" height="62" rx="10" fill="var(--ornament)" opacity="0.6"/>
      <rect class="top-ornament" role="img" aria-label="Gold scroll ornament" x="835" y="228" width="90" height="26" rx="10" fill="var(--ornament)" opacity="0.6"/>
      <rect class="side-ornament" role="img" aria-label="Gold scroll ornament" x="708" y="460" width="26" height="90" rx="10" fill="var(--ornament)" opacity="0.6"/>
      <rect class="side-ornament" role="img" aria-label="Gold scroll ornament" x="1026" y="460" width="26" height="90" rx="10" fill="var(--ornament)" opacity="0.6"/>

      <line class="dot-column" x1="709" y1="315" x2="709" y2="455" stroke="var(--gold)" stroke-width="7" stroke-dasharray="4 12" stroke-linecap="round"/>
      <line class="dot-column" x1="709" y1="585" x2="709" y2="690" stroke="var(--gold)" stroke-width="7" stroke-dasharray="4 12" stroke-linecap="round"/>
      <line class="dot-column" x1="1052" y1="315" x2="1052" y2="455" stroke="var(--gold)" stroke-width="7" stroke-dasharray="4 12" stroke-linecap="round"/>
      <line class="dot-column" x1="1052" y1="585" x2="1052" y2="690" stroke="var(--gold)" stroke-width="7" stroke-dasharray="4 12" stroke-linecap="round"/>

      <rect class="text-panel" x="740" y="268" width="275" height="472" rx="18" fill="url(#backPanel)" stroke="var(--gold)" stroke-width="2"/>

      <g class="star-rule">
        <line x1="787" y1="283" x2="860" y2="283" stroke="var(--gold)" stroke-width="3" stroke-dasharray="3 4"/>
        <line x1="896" y1="283" x2="968" y2="283" stroke="var(--gold)" stroke-width="3" stroke-dasharray="3 4"/>
        <polygon points="878,274 880.6,280.4 887.5,280.9 882.2,285.3 883.9,292 878,288.3 872.1,292 873.8,285.3 868.5,280.9 875.4,280.4" fill="var(--gold)"/>
      </g>
      <g class="star-rule">
        <line x1="787" y1="722" x2="860" y2="722" stroke="var(--gold)" stroke-width="3" stroke-dasharray="3 4"/>
        <line x1="896" y1="722" x2="968" y2="722" stroke="var(--gold)" stroke-width="3" stroke-dasharray="3 4"/>
        <polygon points="878,713 880.6,719.4 887.5,719.9 882.2,724.3 883.9,731 878,727.3 872.1,731 873.8,724.3 868.5,719.9 875.4,719.4" fill="var(--gold)"/>
      </g>

      <g class="back-copy" text-anchor="middle">
        <text class="intro-text" x="877" y="316">Flush fairy is an organic</text>
        <text class="intro-text" x="877" y="339">blend of essential oils that</text>
        <text class="intro-text" x="877" y="362">eliminates the odor when you</text>
        <text class="intro-text" x="877" y="385">poop</text>

        <text class="directions-heading" x="876" y="420">Directions to use:</text>
        <text class="directions-text" x="876" y="447">shake well before each use.</text>
        <text class="directions-text" x="876" y="470">Spray on the toilet water</text>
        <text class="directions-text" x="876" y="493">surface 4-6 times to cover</text>
        <text class="directions-text" x="876" y="516">the water before you go.</text>
        <text class="directions-text" x="876" y="539">Poop as usual and flush.</text>
        <text class="directions-text" x="876" y="562">Safe for all pipes and sewer</text>
        <text class="directions-text" x="876" y="585">systems.</text>

        <text class="keep-text" x="876" y="625">Keep it in the bathroom</text>

        <text class="order-text" x="876" y="660">To order visit my Norvo</text>
        <text class="order-text" x="876" y="683">shop enter flush fairy</text>
      </g>

      <rect class="blossom" role="img" aria-label="Pink cherry blossom flowers" x="970" y="690" width="52" height="50" rx="22" fill="var(--blossom)"/>
    </g>
  </svg>
</div>
</body>
</html>
```